依頼詳細
富山県高岡市「緑ヶ丘市議会」で、明協系会派「明政協和党緑ヶ丘市議会議員会」を結成し、活動を行ってきましたが、それを市民の皆さんにお伝えするために、会報誌を発行したくコンペ方式でデザインをお願いするものです。
宜しくお願い致します。
記載項目
明政協和党緑ヶ丘市議会議員会/090-2846-3917(政調会長森下)/作成料5~10万円
サイズ
B4
ページ数
両面
希望イメージ
シンプル 複雑
単色 カラフル
暗い 明るい
日常 高級
遊び心 厳粛
未来的 伝統的
女性的 男性的
希望する色
赤系、緑系、黄・オレンジ系
納品ファイル
• イラストレーター形式 (.ai)
補足説明
・非常に急いでいます
・ロゴは下記からダウンロードお願いします(ただし、党の広報誌でなく、議会会派の広報誌なので控えめでお願いします)
https://www.sakura-meikyo.jp/policy-koho
https://www.sakura-meikyo.jp/introduction2/pdf/logo_type_A.JPG
デザイン案の提示を使用にも情報が不足しているとのご指摘・ご質問を頂きました。

そこで、掲載する内容(タイトル、文章、写真及びキャプション)を1つのWordデータにまとめました。
また、当方において、手書きで記載したレイアウト案図(表面及び裏面)データ2点を合わせて送付します。

なお、デザインの良さと価格を見て採用を決めたいと思いますので、
その点も踏まえてご提案を宜しくお願いします。
本件は12月10日(木)に開始するも、情報が不足しているとのご意見・ご指摘を受けました。
そこで、12月13日(日)夜中に、掲載頂きたい情報(文章や写真及びキャプションなど)を追記したところです。

今般、当該内容について、少しだけ修正を加えました。
修正箇所は分かりやすいように黄色に着色又は黄色の枠で囲ってありますので、ご確認の上、既に提出の方は修正対応頂ければ幸いに存じます。
未提出の方は、今回のデータを元にデザイン案を作成願います。

なお、仮に修正対応されなかったとしても、レイアウトの案をご提示いただいていますので、それでもって、私たちの会派の政務調査会を開催し、採用デザイン案を週明け12月22日(月)に決定する予定です。

以上、宜しくお願い致します。
■ 選んだ理由

シンプルで明瞭なデザイン、色使いで、パッと見て目につきやすい印象を受けました。
今回の私たちの目的が、多くの市民の皆さまにご覧頂くことであり、その観点から一番最適であると判断した次第です。

■ 提案者全員のお礼・コメント

年末の依頼で、皆さまお忙しい中、多くのご提案を頂きました。
そして提案のどれもが、非常に質が高く、驚きと感動をもって全提案を拝見させて頂きました。
残念ながら、選定できるのは1点であり、選定できなかった皆さま方には誠に申し訳ございません。

なお、今回初の会派広報紙の発行、そしてクリエモールの活用であり、今後もし仕事を依頼することがありましたら、その際にはぜひご協力頂ければ幸いに存じます。

皆さまのご健康とご多幸、そして良い年を迎えられるよう祈念申し上げ御礼のコメントとします。
誠にありがとうございました。

```html
<!DOCTYPE html>
<html lang="ja">
<head>
<meta charset="utf-8">
<title>明政協和党緑ヶ丘市議会議員会 活動報告</title>
<link href="https://fonts.googleapis.com/css2?family=Noto+Sans+JP:wght@400;500;700;900&display=swap" rel="stylesheet">
<style>
:root{
  --green:#2f9a3c;
  --green-dark:#1f7a2c;
  --green-pale:#e4f2dc;
  --orange:#ee8a1c;
  --red:#d8362a;
  --ink:#222;
  --paper:#fff;
  --photo-a:#c9cfd6;
  --photo-b:#8d96a2;
}
*{box-sizing:border-box;margin:0;padding:0}
html,body{width:847px;height:1200px;overflow:hidden;background:var(--paper)}
body{font-family:"Noto Sans JP",sans-serif;color:var(--ink);position:relative}
.masthead{position:absolute;left:0;top:0;width:847px;height:110px;border-bottom:4px solid var(--green)}
.council{position:absolute;left:22px;top:24px;display:flex;align-items:center;gap:6px;color:var(--green);font-weight:700;font-size:16px;white-space:nowrap}
.council .dot{width:20px;height:20px;border-radius:50%;background:var(--green)}
.group-title{position:absolute;left:150px;top:16px;width:545px;font-size:28px;line-height:40px;font-weight:900;white-space:nowrap}
.report-badge{position:absolute;right:20px;top:14px;width:118px;height:78px;background:var(--green);color:#fff;text-align:center;font-weight:900;padding-top:8px;line-height:1.2}
.report-badge .party{font-size:28px;display:block}
.report-badge .sub{font-size:17px}
.members-band{position:absolute;left:0;top:114px;width:847px;height:34px;background:var(--green-pale);text-align:center}
.pill{display:inline-block;margin-top:4px;background:var(--green);color:#fff;font-weight:700;font-size:16px;padding:2px 28px;border-radius:14px;letter-spacing:2px}
.members{position:absolute;left:22px;top:160px;width:803px;display:grid;grid-template-columns:repeat(8,1fr);row-gap:14px}
.member{text-align:center}
.photo{width:82px;height:82px;border-radius:50%;margin:0 auto;background:radial-gradient(circle at 50% 35%,var(--photo-a),var(--photo-b))}
.role{font-size:10px;margin-top:5px;color:#555;height:13px}
.name{font-size:13px;font-weight:500}
.section-head{position:absolute;left:30px;top:462px;width:787px;text-align:center;font-size:25px;font-weight:900;color:var(--red);border-bottom:2px solid var(--green);padding-bottom:6px}
.intro{position:absolute;left:40px;top:510px;width:767px;font-size:14px;line-height:1.85;text-align:justify}
.activities-band{position:absolute;left:0;top:672px;width:847px;height:58px;background:var(--green);color:#fff;font-size:25px;font-weight:900;text-align:center;line-height:58px}
.activities-band::after{content:"";position:absolute;left:50%;bottom:-12px;margin-left:-14px;border:14px solid transparent;border-bottom:0;border-top-color:var(--green)}
.item-head{position:absolute;left:30px;display:flex;align-items:center;gap:12px;font-size:22px;font-weight:900;color:var(--red);width:787px;border-bottom:2px dotted var(--orange);padding-bottom:4px}
.num{width:40px;height:40px;border-radius:50%;background:var(--orange);color:#fff;font-size:24px;text-align:center;line-height:40px;flex:none}
.item-one{top:752px}
.item-two{top:896px}
.item-text{position:absolute;font-size:13.5px;line-height:1.8;text-align:justify}
.item-one-text{left:40px;top:806px;width:767px}
.item-two-text{left:40px;top:950px;width:580px}
.building-photo{position:absolute;left:640px;top:946px;width:180px;height:170px;background:linear-gradient(160deg,#c8ddee,#9fb4a0)}
.caption{position:absolute;left:640px;top:1120px;width:180px;font-size:10px;color:#555;line-height:1.4}
.next-page{position:absolute;right:26px;top:1160px;background:var(--green);color:#fff;font-size:13px;font-weight:700;padding:5px 14px;border-radius:3px}
</style>
</head>
<body>
<header class="masthead">
  <div class="council"><span class="dot"></span>緑ヶ丘市議会</div>
  <h1 class="group-title">「明政協和党緑ヶ丘市議会議員会」</h1>
  <div class="report-badge"><span class="party">明協党</span><span class="sub">活動報告</span></div>
</header>

<div class="members-band"><span class="pill">会派構成員紹介</span></div>

<section class="members">
  <div class="member"><div class="photo" role="img" aria-label="議員の肖像写真"></div><p class="role">副議長</p><p class="name">島 弘志</p></div>
  <div class="member"><div class="photo" role="img" aria-label="議員の肖像写真"></div><p class="role">会長</p><p class="name">高木 一夫</p></div>
  <div class="member"><div class="photo" role="img" aria-label="議員の肖像写真"></div><p class="role">幹事長</p><p class="name">菅原 和彦</p></div>
  <div class="member"><div class="photo" role="img" aria-label="議員の肖像写真"></div><p class="role">政調会長</p><p class="name">森下 誠一</p></div>
  <div class="member"><div class="photo" role="img" aria-label="議員の肖像写真"></div><p class="role">総務会長</p><p class="name">瀬戸 悟</p></div>
  <div class="member"><div class="photo" role="img" aria-label="議員の肖像写真"></div><p class="role"></p><p class="name">福本 直</p></div>
  <div class="member"><div class="photo" role="img" aria-label="議員の肖像写真"></div><p class="role"></p><p class="name">梶原 正志</p></div>
  <div class="member"><div class="photo" role="img" aria-label="議員の肖像写真"></div><p class="role"></p><p class="name">中川 佳代子</p></div>
  <div class="member"><div class="photo" role="img" aria-label="議員の肖像写真"></div><p class="role"></p><p class="name">藤井 一光</p></div>
  <div class="member"><div class="photo" role="img" aria-label="議員の肖像写真"></div><p class="role"></p><p class="name">酒井 洋平</p></div>
  <div class="member"><div class="photo" role="img" aria-label="議員の肖像写真"></div><p class="role"></p><p class="name">石原 克也</p></div>
  <div class="member"><div class="photo" role="img" aria-label="議員の肖像写真"></div><p class="role"></p><p class="name">金沢 宏明</p></div>
  <div class="member"><div class="photo" role="img" aria-label="議員の肖像写真"></div><p class="role"></p><p class="name">中村 真治</p></div>
  <div class="member"><div class="photo" role="img" aria-label="議員の肖像写真"></div><p class="role"></p><p class="name">林 貴文</p></div>
  <div class="member"><div class="photo" role="img" aria-label="議員の肖像写真"></div><p class="role"></p><p class="name">浅井 哲也</p></div>
  <div class="member"><div class="photo" role="img" aria-label="議員の肖像写真"></div><p class="role"></p><p class="name">西田 恵美</p></div>
</section>

<h2 class="section-head">市議会、そして会派の活動・役割について</h2>
<p class="intro">市の運営に必要な予算や、あらゆる条例の制定・改廃などを審議し、決定する市議会は、市民の皆さまの声を市政へ届ける大切な場です。議会の中では、同じ考えを持つ議員が集まり「会派」をつくり、政策を話し合い、まとまった力で市への提言を行っています。私たち明政協和党緑ヶ丘市議会議員会は、市議会最大の会派として、市民の皆さまの暮らしに寄り添い、安心と活力あるまちづくりを進めるため、日々の議会活動に取り組んでまいりました。ここに、これまでの主な活動をご報告いたします。</p>

<div class="activities-band">結成から1年。これまでの私たちの主な活動について</div>

<h3 class="item-head item-one"><span class="num">1</span>「新型コロナウイルス感染症」に対応！</h3>
<p class="item-text item-one-text">新型コロナウイルス感染症の拡大を受け、会派として市長へ緊急要望を行い、医療体制の確保や検査の充実、事業者・家庭への支援策の拡充を求めました。その結果、市独自の給付金や相談窓口の設置など、多くの提言が実現しています。今後も感染の状況を注視し、市民の皆さまの命と暮らしを守る取り組みを続けてまいります。</p>

<h3 class="item-head item-two"><span class="num">2</span>駅前旧ミリエへの市役所本庁舎全面移転を提言！</h3>
<p class="item-text item-two-text">老朽化が進む市役所本庁舎のあり方について、会派内で何度も協議を重ねてきました。耐震性や維持費、駅前のにぎわいづくりなど様々な観点から検討した結果、空き店舗となっている駅前の旧ミリエへ本庁舎を全面移転することが最も効果的であるとの結論に至り、市長へ提言を行いました。建物の有効活用により、整備費用を大きく抑えることができるとともに、交通の便が良い場所で市民サービスの向上も期待されます。今後も市民の皆さまのご意見を伺いながら、将来を見据えた最善の形を目指して議論を深めてまいります。</p>
<div class="building-photo" role="img" aria-label="駅前旧ミリエの建物外観写真"></div>
<p class="caption">移転を提言した駅前の旧ミリエ</p>

<div class="next-page">続きは、裏面をご覧ください。</div>
</body>
</html>
```